Music Industry Business Needs a Business Card Design

Copper Lantern is an audio mastering company that has been in business for 20 years. Mastering is the final creative step in the music production chain. Our job is to make the music sound as good as it possibly can prior to release to the public. Our world is technical, artistic, precise. We work on everything from independent artists to the music for the Grandfield Cup. We are looking for a new, more modern business card design. I am uploading a copy of our logo, although it doesn't absolutely need to be included in the design.

Target Market(s)

Music Industry Professionals

Industry/Entity Type

Business

Contact Information for Business Card

Address, Phone, Email, Website, Name, Job Title

Font styles to use
Sans Serif

Requirements
Must have
• Sorry, but I don't have any concrete things to request. If I had a clear idea of what I want, I would probably just design something myself. I am looking for fresh input and thought I would try this.
Should not have
• Anything that is typical, such as headphones or the like.

```html
<!DOCTYPE html>
<html lang="en">
<head>
<meta charset="utf-8">
<title>Copper Lantern – Business Card</title>
<link rel="stylesheet" href="https://fonts.googleapis.com/css2?family=Open+Sans:ital,wght@0,400;0,600;0,700;1,400&display=swap">
<style>
  :root {
    --backdrop: #c6c7c9;
    --navy: #163f73;
    --navy-deep: #123461;
    --cyan: #3bc1e8;
    --teal: #7fd0d6;
    --white: #ffffff;
  }
  * { margin: 0; padding: 0; box-sizing: border-box; }
  html, body {
    width: 1200px; height: 848px; overflow: hidden;
    background: var(--backdrop);
    font-family: "Open Sans", Arial, sans-serif;
  }
  .card {
    position: absolute; left: 195px; top: 155px;
    width: 787px; height: 485px;
    border-radius: 23px; overflow: hidden;
    background: var(--white);
    box-shadow: 0 10px 14px -8px rgba(0,0,0,0.25);
  }
  .brand-panel {
    position: absolute; left: 0; top: 0;
    width: 393px; height: 485px;
    background: var(--navy);
  }
  .brand-artwork {
    position: absolute; left: 0; top: 252px;
    width: 393px; height: 233px;
    background: linear-gradient(160deg, var(--teal) 0%, var(--cyan) 45%, var(--navy) 100%);
  }
  .brand-name {
    position: absolute; top: 20px; left: 0; width: 393px;
    text-align: center; color: var(--white);
    font-size: 31px; font-weight: 400; letter-spacing: 2px;
  }
  .brand-tagline {
    position: absolute; top: 60px; left: 0; width: 393px;
    text-align: center; color: var(--cyan);
    font-size: 18px; font-style: italic;
  }
  .person { position: absolute; right: 14px; text-align: right; color: var(--white); font-weight: 700; font-size: 20px; }
  .person-name { top: 178px; }
  .person-title { top: 218px; }
  .contact {
    position: absolute; left: 436px; width: 308px; height: 63px;
    border-radius: 32px; display: flex; align-items: center;
    padding-left: 16px; font-size: 16px; font-weight: 600;
    white-space: nowrap;
  }
  .contact svg { width: 44px; height: 44px; flex: none; margin-right: 14px; }
  .contact-phone { top: 63px; background: var(--navy); color: var(--cyan); }
  .contact-email { top: 163px; background: var(--teal); color: var(--navy); font-weight: 400; }
  .contact-web { top: 263px; background: var(--cyan); color: var(--navy); font-weight: 400; }
  .contact-address { top: 362px; background: var(--navy); color: var(--cyan); font-size: 14px; line-height: 1.2; }
</style>
</head>
<body>
<div class="card">
  <div class="brand-panel">
    <div class="brand-artwork" role="img" aria-label="Decorative flowing blue wave artwork"></div>
    <div class="brand-name">COPPER LANTERN</div>
    <div class="brand-tagline">Finest Quality Audio Mastering</div>
    <div class="person person-name">Your Name</div>
    <div class="person person-title">Job Title</div>
  </div>

  <div class="contact contact-phone">
    <svg viewBox="0 0 44 44"><path d="M10 8 C6 12 6 20 14 29 C22 37 31 39 36 35 L31 28 L26 30 C22 28 17 23 15 19 L17 14 Z" fill="var(--cyan)"/></svg>
    (403) 555 - 0187
  </div>
  <div class="contact contact-email">
    <svg viewBox="0 0 44 44"><rect x="5" y="11" width="34" height="22" fill="var(--white)"/><path d="M5 11 L22 25 L39 11 M5 33 L17 21 M39 33 L27 21" stroke="var(--teal)" stroke-width="2" fill="none"/></svg>
    email@copperlantern.com
  </div>
  <div class="contact contact-web">
    <svg viewBox="0 0 44 44" fill="none" stroke="var(--navy)" stroke-width="2.5"><circle cx="22" cy="22" r="15"/><ellipse cx="22" cy="22" rx="6.5" ry="15"/><path d="M7 22 H37 M9 14 H35 M9 30 H35"/></svg>
    www.copperlantern.ca/
  </div>
  <div class="contact contact-address">
    <svg viewBox="0 0 44 44"><path d="M4 22 L22 6 L40 22 L36 22 L36 38 L26 38 L26 28 L18 28 L18 38 L8 38 L8 22 Z" fill="var(--cyan)"/></svg>
    <span>218 - 7th Avenue S.W.<br>Calgary, Alberta, Canada<br>T2P 0K5</span>
  </div>
</div>
</body>
</html>
```